Website Update for Global Company - Solar Technology - Brisqell

We recently released our first version of our website kelvaris.com. However despite a longer process of developing the page, it is still missing the elements of a brilliant website. (Currently it looks dead and boring) We are having problems integrating our logo and want to create a more catching site. The task involves an updated and without changing most of main elements in the existing page. (Unless you can do it even better) The blue color needs to be kept but can be changed within the blue-spectrum. The logo text (KELVARIS) must be better integrated in the site, however the main logo could be used in elements like we have tried with the background. The surface of the logo could be changed to 3D or metallic, or any other theme that would make the site more complete.
It would be good if some elements of the site could be used on business cards and invoices to keep the company identity.
Kelvaris is a new development company specialized in green energy and sustainable development. We do design, engineering, manufacturing, sourcing and other processes related to product development – both as consultants and for own products.
Keep the look of the site as professional as possible, and with a cooperate-looking style.

Link to existing page: www.kelvaris.com

Brief Update : After reviewing the designs we would like all new and current designers to make more bold designs that stands out from the rest. We do not like the standard layout that looks like any other cooperate homepage. We want a very unique and very lively page - with faded images and effects when hoovering like seen on our existing page. Try make all elements blend together, and use faded background images instead of just white color - or something else.

Make the site unique !

Industry/Entity Type

Solar Energy

Contact Information for Business Card

Owner/Founder/CEO : Frederik Lysgaard Holm
Company name: Kelvaris ApS
Email: frederik.lysgaard@kelvaris.dk
Phone: +45 71 83 96 54
Slogan Sustainable Development
Address: Havnestien 18, 2
DK-5820 Svendborg, Denmark

Number of Pages Required

3 page

Font styles to use
Serif
Sans Serif

Colors
0555a3
85acd3
cedeed
3176b5
cee9f5
85cae6
0293ce
86cfc6
33b8a4

```html
<!DOCTYPE html>
<html lang="en">
<head>
<meta charset="utf-8">
<title>Kelvaris – Sustainable Development</title>
<link href="https://fonts.googleapis.com/css2?family=Raleway:wght@400;500;600;700&family=Open+Sans:wght@400;600&display=swap" rel="stylesheet">
<style>
:root{
  --blue:#0293ce;
  --blue-deep:#0555a3;
  --blue-mid:#3176b5;
  --blue-soft:#85cae6;
  --ice:#cee9f5;
  --ink:#1f2a36;
  --text:#5b6470;
  --grey-bg:#eef1f4;
  --dark:#1b1e22;
  --white:#ffffff;
  --red:#d8283c;
  --navy:#2f4a6a;
}
*{box-sizing:border-box;margin:0;padding:0}
html,body{width:1200px;height:2832px;overflow:hidden}
body{position:relative;background:var(--grey-bg);font-family:"Open Sans",Arial,sans-serif;color:var(--text)}
.abs{position:absolute}
h1,h2,h3,.nav a,.tile-title,.brand{font-family:"Raleway",Arial,sans-serif}

/* Header & hero */
.hero{left:0;top:0;width:1200px;height:760px;background:linear-gradient(180deg,#9ea3a8 0%,#d3d6d9 35%,#e9ebed 70%,#f2f3f5 100%)}
.hero-photo{left:0;top:0;width:1200px;height:760px;background:radial-gradient(ellipse at 45% 20%,rgba(255,255,255,.55),rgba(255,255,255,0) 55%),linear-gradient(120deg,rgba(120,128,138,.5),rgba(230,232,235,.1) 60%)}
.brand{display:flex;align-items:center;gap:14px;left:40px;top:32px;font-size:46px;font-weight:700;color:#3a3f45;letter-spacing:2px}
.brand .mark{width:46px;height:46px;background:var(--blue-deep)}
.nav{right:40px;top:52px;display:flex;gap:38px}
.nav a{font-size:14px;font-weight:600;color:#444;text-decoration:none;letter-spacing:.5px}
.nav a.active{color:var(--blue)}
.hero-title{left:0;top:350px;width:1200px;text-align:center;font-size:36px;font-weight:600;color:var(--ink);line-height:46px;letter-spacing:.5px}

/* Services */
.service{top:525px;width:188px;height:196px;background:rgba(255,255,255,.9);text-align:center}
.service .icon{width:110px;height:110px;border-radius:50%;background:var(--blue);margin:22px auto 0;display:flex;align-items:center;justify-content:center}
.service p{margin-top:26px;font-family:"Raleway",sans-serif;font-size:16px;font-weight:600;color:var(--blue);letter-spacing:.5px}
.plus{top:590px;width:60px;text-align:center;font-size:40px;color:var(--white);font-weight:600}

/* Feature cards */
.feature{top:758px;width:546px;height:200px;background:var(--white);box-shadow:0 2px 8px rgba(0,0,0,.08)}
.feature .pic{left:14px;top:14px;width:196px;height:172px}
.feature h3{left:228px;top:16px;font-size:17px;font-weight:700;color:var(--blue)}
.feature p{left:228px;top:44px;width:296px;font-size:12px;line-height:18px;color:var(--text)}
.btn{left:228px;top:152px;width:96px;height:30px;background:var(--blue);color:var(--white);font-size:12px;font-weight:600;display:flex;align-items:center;justify-content:center}

/* Videos */
.videos{left:0;top:1000px;width:1200px;height:258px;background:linear-gradient(180deg,#3a3e44,#22252a)}
.videos h2{left:0;top:44px;width:1200px;text-align:center;font-size:30px;font-weight:600;color:var(--white)}
.play{left:564px;top:108px}

/* Tiles */
.tile{overflow:hidden}
.tile .fill{left:0;top:0;width:100%;height:100%}
.tile-title{position:absolute;left:0;width:100%;text-align:center;color:var(--white);font-size:28px;font-weight:600;line-height:34px;text-shadow:0 1px 4px rgba(0,0,0,.5)}
.arrow{position:absolute;width:40px;height:40px;background:var(--white);display:flex;align-items:center;justify-content:center;bottom:14px;left:50%;margin-left:-20px}

/* News */
.news{left:0;top:2240px;width:1200px;height:235px;background:var(--blue)}
.news h2{left:0;top:26px;width:1200px;text-align:center;font-size:28px;font-weight:600;color:var(--white)}
.news-item{top:92px;width:354px;height:104px;border:1px solid rgba(255,255,255,.5)}
.date{left:18px;top:18px;width:66px;height:66px;background:var(--white);text-align:center;color:var(--blue-deep);font-family:"Raleway",sans-serif}
.date b{display:block;font-size:22px;margin-top:6px}
.date span{font-size:13px;font-weight:700}
.news-item p{left:106px;top:40px;color:var(--white);font-size:15px}

/* Social */
.social{left:0;top:2475px;width:1200px;height:190px;background:#e6ebf0}
.social h2{left:0;top:28px;width:1200px;text-align:center;font-size:28px;font-weight:700;color:var(--blue)}
.soc-btn{top:90px;width:264px;height:52px;color:var(--white);font-family:"Raleway",sans-serif;font-size:20px;font-weight:700;display:flex;align-items:center;justify-content:center;gap:12px}
.soc-btn i{width:12px;height:12px;background:var(--white);display:block}
.soc-count{top:150px;width:264px;text-align:center;font-size:12px;color:#7a8390}

/* Contact & footer */
.contact{left:0;top:2665px;width:1200px;height:92px;background:#2b2f35;display:flex;justify-content:center;align-items:center;gap:90px;color:var(--white);font-size:24px}
.contact span{display:flex;align-items:center;gap:16px}
.footer{left:0;top:2757px;width:1200px;height:75px;background:var(--dark)}
.footer .brand{left:40px;top:18px;font-size:32px;color:var(--white);gap:10px}
.footer .brand .mark{width:32px;height:32px;background:var(--blue)}
.footer p{left:0;top:28px;width:1200px;text-align:center;font-size:13px;color:#9aa1aa}
</style>
</head>
<body>

<!-- Header & hero -->
<div class="abs hero"></div>
<div class="abs hero-photo" role="img" aria-label="Photo of a hand touching a glowing digital interface of floating panels"></div>
<div class="abs brand"><span class="mark"></span>KELVARIS</div>
<nav class="abs nav">
  <a class="active" href="#">HOME</a><a href="#">EXPERTISE</a><a href="#">APPROACH</a><a href="#">CLIENTS</a><a href="#">ABOUT</a><a href="#">CONTACT</a>
</nav>
<h1 class="abs hero-title">WE PROVIDE COMPLETE SERVICES THROUGHOUT<br>THE PRODUCT DEVELOPMENT PROCESS</h1>

<!-- Services -->
<div class="abs service" style="left:46px">
  <div class="icon"><svg width="46" height="46" viewBox="0 0 46 46"><rect x="6" y="6" width="34" height="34" rx="3" fill="none" stroke="#fff" stroke-width="4"/><circle cx="17" cy="17" r="4" fill="#fff"/><path d="M10 36 L20 24 L27 31 L32 26 L38 36Z" fill="#fff"/></svg></div>
  <p>DESIGN</p>
</div>
<div class="abs plus" style="left:238px">+</div>
<div class="abs service" style="left:302px">
  <div class="icon"><svg width="46" height="46" viewBox="0 0 46 46"><path d="M16 40 V14 a7 7 0 0 1 14 0 V32" fill="none" stroke="#fff" stroke-width="4" stroke-linecap="round"/><path d="M23 6 V40" stroke="#fff" stroke-width="4" stroke-linecap="round"/></svg></div>
  <p>ENGINEERING</p>
</div>
<div class="abs plus" style="left:494px">+</div>
<div class="abs service" style="left:648px">
  <div class="icon"><svg width="52" height="46" viewBox="0 0 52 46"><g fill="#fff"><path d="M26 2 L38 8 L26 14 L14 8Z"/><path d="M14 10 L25 16 V28 L14 22Z"/><path d="M38 10 L27 16 V28 L38 22Z"/><path d="M14 24 L25 30 V44 L14 38Z" opacity=".9"/><path d="M38 24 L27 30 V44 L38 38Z" opacity=".9"/><path d="M2 24 L12 19 V33 L2 38Z"/><path d="M50 24 L40 19 V33 L50 38Z"/></g></svg></div>
  <p>SOURCING</p>
</div>
<div class="abs plus" style="left:878px">+</div>
<div class="abs service" style="left:966px">
  <div class="icon"><svg width="50" height="50" viewBox="0 0 50 50"><g fill="none" stroke="#fff" stroke-width="5"><circle cx="19" cy="30" r="9"/><circle cx="36" cy="14" r="6"/></g><g stroke="#fff" stroke-width="5" stroke-linecap="round"><path d="M19 15v4M19 41v4M4 30h4M30 30h4M8 19l3 3M27 38l3 3M8 41l3-3M27 22l3-3"/><path d="M36 3v3M36 22v3M25 14h3M44 14h3"/></g></svg></div>
  <p>MANUFACTURING</p>
</div>

<!-- Feature cards -->
<div class="abs feature" style="left:46px">
  <div class="abs pic" role="img" aria-label="Photo of a woman working at a laptop in a bright office" style="background:linear-gradient(135deg,#e8e6e2,#c9c4bd 60%,#a9a39b)"></div>
  <h3 class="abs">FEATURE INNOVATION</h3>
  <p class="abs">Our team turns early ideas into working solar products through careful study, quick testing and close work with partners.</p>
  <div class="abs btn">Read More</div>
</div>
<div class="abs feature" style="left:608px">
  <div class="abs pic" role="img" aria-label="Photo of a tablet computer lying on a desk beside a keyboard" style="background:linear-gradient(135deg,#f2f2f2,#cfd4d9 55%,#6c7a88)"></div>
  <h3 class="abs">OUR WORK</h3>
  <p class="abs">See how we guide each project from first sketch to final product, with clear steps and shared goals.</p>
  <div class="abs btn">Read More</div>
</div>

<!-- Project videos -->
<div class="abs videos" role="img" aria-label="Faded photo of an engineering workshop behind the video section"></div>
<div class="abs" style="left:0;top:1000px;width:1200px;height:258px">
  <h2 class="abs" style="left:0;top:44px;width:1200px;text-align:center;font-size:30px;font-weight:600;color:#fff">PROJECT VIDEOS</h2>
  <svg class="abs play" width="72" height="72" viewBox="0 0 72 72"><circle cx="36" cy="36" r="32" fill="none" stroke="#fff" stroke-width="4"/><path d="M29 22 L51 36 L29 50Z" fill="#fff"/></svg>
</div>

<!-- Tiles row 1 -->
<div class="abs tile" style="left:46px;top:1290px;width:362px;height:284px">
  <div class="abs fill" role="img" aria-label="Photo of a glowing globe held in hands" style="background:radial-gradient(circle at 60% 55%,#c98a3a,#5a3a22 55%,#2a1d16)"></div>
  <div class="tile-title" style="top:120px">FOCUSED INNOVATION</div>
  <div class="arrow"><svg width="12" height="16" viewBox="0 0 12 16"><path d="M2 2 L9 8 L2 14" fill="none" stroke="#555" stroke-width="2.5"/></svg></div>
</div>
<div class="abs tile" style="left:418px;top:1290px;width:364px;height:284px">
  <div class="abs fill" role="img" aria-label="Blue-tinted photo of industrial design sketches" style="background:linear-gradient(135deg,#7fc2ea,#2f8fd0 55%,#1a6fb4)"></div>
  <div class="tile-title" style="top:120px">INDUSTRIAL DESIGN</div>
  <div class="arrow"><svg width="12" height="16" viewBox="0 0 12 16"><path d="M2 2 L9 8 L2 14" fill="none" stroke="#555" stroke-width="2.5"/></svg></div>
</div>
<div class="abs tile" style="left:792px;top:1290px;width:362px;height:284px">
  <div class="abs fill" role="img" aria-label="Photo of a blue globe with science icons" style="background:radial-gradient(circle at 50% 45%,#3d8ec2,#1a4b6e 55%,#0f2a40)"></div>
  <div class="tile-title" style="top:104px">SCIENCE &amp;<br>TECHNOLOGY</div>
  <div class="arrow"><svg width="12" height="16" viewBox="0 0 12 16"><path d="M2 2 L9 8 L2 14" fill="none" stroke="#555" stroke-width="2.5"/></svg></div>
</div>

<!-- Tiles row 2 -->
<div class="abs tile" style="left:46px;top:1586px;width:552px;height:340px">
  <div class="abs fill" role="img" aria-label="Photo of a team gathered around a laptop discussing a project" style="background:linear-gradient(135deg,#b9bec4,#7d858e 55%,#4b525a)"></div>
  <div class="tile-title" style="top:124px">WE ARE LOOKING FOR<br>NEW PROBLEM TO SOLVE</div>
  <div class="arrow"><svg width="12" height="16" viewBox="0 0 12 16"><path d="M2 2 L9 8 L2 14" fill="none" stroke="#555" stroke-width="2.5"/></svg></div>
</div>
<div class="abs tile" style="left:608px;top:1586px;width:546px;height:340px">
  <div class="abs fill" role="img" aria-label="Photo of a manufacturing floor with machinery" style="background:linear-gradient(135deg,#d9dde1,#a6adb5 55%,#6f7882)"></div>
  <div class="tile-title" style="top:124px">MANUFACTURING<br>DEVELOPMENT</div>
  <div class="arrow"><svg width="12" height="16" viewBox="0 0 12 16"><path d="M2 2 L9 8 L2 14" fill="none" stroke="#555" stroke-width="2.5"/></svg></div>
</div>

<!-- Tiles row 3 -->
<div class="abs tile" style="left:46px;top:1938px;width:270px;height:284px">
  <div class="abs fill" role="img" aria-label="Photo of an industrial prototype machine" style="background:linear-gradient(135deg,#4b6a86,#26384a)"></div>
  <div class="tile-title" style="top:104px;font-size:25px">PROTATYPE<br>DEVELOPMENT</div>
  <div class="arrow"><svg width="12" height="16" viewBox="0 0 12 16"><path d="M2 2 L9 8 L2 14" fill="none" stroke="#555" stroke-width="2.5"/></svg></div>
</div>
<div class="abs tile" style="left:326px;top:1938px;width:270px;height:284px">
  <div class="abs fill" role="img" aria-label="Photo of an electrical circuit board" style="background:linear-gradient(135deg,#4a5a6a,#1f2a35)"></div>
  <div class="tile-title" style="top:104px;font-size:25px">ELECTRICAL<br>ENGINEERING</div>
  <div class="arrow"><svg width="12" height="16" viewBox="0 0 12 16"><path d="M2 2 L9 8 L2 14" fill="none" stroke="#555" stroke-width="2.5"/></svg></div>
</div>
<div class="abs tile" style="left:606px;top:1938px;width:270px;height:284px">
  <div class="abs fill" role="img" aria-label="Photo of a maker workspace with tools" style="background:linear-gradient(135deg,#3a3d42,#1c1e21)"></div>
  <div class="tile-title" style="top:104px;font-size:25px">MAKER SPACE<br>COMING SOON</div>
  <div class="arrow"><svg width="12" height="16" viewBox="0 0 12 16"><path d="M2 2 L9 8 L2 14" fill="none" stroke="#555" stroke-width="2.5"/></svg></div>
</div>
<div class="abs tile" style="left:886px;top:1938px;width:268px;height:284px">
  <div class="abs fill" role="img" aria-label="Photo of an assembly line with a red light" style="background:linear-gradient(135deg,#5a5f66,#2b2e33 60%,#6a2a30)"></div>
  <div class="tile-title" style="top:104px;font-size:25px">MANUFACTURING<br>DEVELOPMENT</div>
  <div class="arrow"><svg width="12" height="16" viewBox="0 0 12 16"><path d="M2 2 L9 8 L2 14" fill="none" stroke="#555" stroke-width="2.5"/></svg></div>
</div>

<!-- News -->
<section class="abs news">
  <h2 class="abs">IN THE NEWS</h2>
  <div class="abs news-item" style="left:46px"><div class="abs date"><b>29</b><span>AUG</span></div><p class="abs">Launch of website</p></div>
  <div class="abs news-item" style="left:423px"><div class="abs date"><b>29</b><span>AUG</span></div><p class="abs">First project initiated</p></div>
  <div class="abs news-item" style="left:800px"><div class="abs date"><b>29</b><span>AUG</span></div><p class="abs">Establishment of Kelvaris ApS</p></div>
</section>

<!-- Social -->
<section class="abs social">
  <h2 class="abs">FOLLOW US TO STAY IN TOUCH</h2>
  <div class="abs soc-btn" style="left:76px;background:var(--blue-deep)"><i></i>Friendloop</div>
  <div class="abs soc-btn" style="left:352px;background:var(--blue)"><i></i>Chirpline</div>
  <div class="abs soc-btn" style="left:628px;background:var(--navy)"><i></i>Workgrid</div>
  <div class="abs soc-btn" style="left:904px;background:var(--red)"><i></i>Snapframe</div>
  <div class="abs soc-count" style="left:76px">2,318 Followers</div>
  <div class="abs soc-count" style="left:352px">2,318 Followers</div>
  <div class="abs soc-count" style="left:628px">2,318 Followers</div>
  <div class="abs soc-count" style="left:904px">2,318 Followers</div>
</section>

<!-- Contact -->
<div class="abs contact">
  <span><svg width="26" height="26" viewBox="0 0 26 26"><path d="M6 2 L10 2 L12 8 L9 10 C10 14 12 16 16 17 L18 14 L24 16 L24 20 C24 22 22 24 20 24 C10 23 3 16 2 6 C2 4 4 2 6 2Z" fill="#fff"/></svg>123.456.7890</span>
  <span><svg width="28" height="20" viewBox="0 0 28 20"><rect x="1" y="1" width="26" height="18" fill="none" stroke="#fff" stroke-width="2"/><path d="M1 1 L14 11 L27 1" fill="none" stroke="#fff" stroke-width="2"/></svg>info@companyname.com</span>
</div>

<!-- Footer -->
<footer class="abs footer">
  <div class="abs brand"><span class="mark"></span>KELVARIS</div>
  <p class="abs">All Right Reserved Copyright ©2014 Kelvaris</p>
</footer>

</body>
</html>
```